Roof Plumbing Company needs simple, modern business card using the attached logo and below details:

Dean Halloway
Summit Gutters Pty Ltd
ABN: 58 214 937 062
Phone: 0417 286 531
Email: summitgutters@mailbrook.com
Website: summitgutters.com.au

For all of your metal roof plumbing requirements contact Summit Gutters for an obligation free quote - no job too big or to small!

Industry/Entity Type

Business

Contact Information for Business Card

Dean Halloway
Summit Gutters Pty Ltd
ABN 58 214 937 062
0417 286 531
summitgutters@mailbrook.com
summitgutters.com.au

Requirements
Must have
• Bright eye catching design, professional look

```html
<!DOCTYPE html>
<html lang="en">
<head>
<meta charset="utf-8">
<title>Summit Gutters Pty Ltd – Business Card</title>
<link href="https://fonts.googleapis.com/css2?family=Open+Sans:wght@400;600;700&display=swap" rel="stylesheet">
<style>
  :root {
    --backdrop: #e9e7e4;
    --card-black: #161616;
    --card-charcoal: #262626;
    --brand-red: #e10f0f;
    --deep-red: #8c0606;
    --text-white: #ffffff;
    --text-soft: #e6e6e6;
  }
  * { box-sizing: border-box; margin: 0; padding: 0; }
  html, body {
    width: 1200px;
    height: 844px;
    overflow: hidden;
    background: var(--backdrop);
    font-family: "Open Sans", Arial, sans-serif;
  }
  .canvas {
    width: 1200px;
    height: 844px;
    display: flex;
    align-items: center;
    justify-content: center;
    gap: 56px;
  }
  .card {
    position: relative;
    width: 520px;
    height: 298px;
    background: radial-gradient(ellipse at 50% 35%, var(--card-charcoal) 0%, var(--card-black) 75%);
    box-shadow: 0 10px 28px rgba(0,0,0,0.28);
    overflow: hidden;
    color: var(--text-white);
  }

  /* Contact side */
  .band {
    position: absolute;
    left: 0;
    right: 0;
    height: 16px;
    background: linear-gradient(180deg, var(--brand-red), #b80909);
  }
  .band--top { top: 0; border-bottom: 3px solid var(--deep-red); }
  .band--bottom { bottom: 0; border-top: 3px solid var(--deep-red); }
  .contact {
    position: absolute;
    inset: 0;
    display: flex;
    flex-direction: column;
    align-items: center;
    text-align: center;
    padding-top: 72px;
  }
  .contact__name {
    color: var(--brand-red);
    font-size: 20px;
    font-weight: 600;
    margin-bottom: 28px;
  }
  .contact__abn {
    font-size: 17px;
    font-weight: 700;
    margin-bottom: 22px;
  }
  .contact__abn-label { color: var(--brand-red); }
  .contact__line {
    font-size: 15px;
    color: var(--text-soft);
    line-height: 1.45;
  }

  /* Brand side */
  .tab {
    position: absolute;
    width: 22px;
    height: 40px;
    background: linear-gradient(180deg, var(--brand-red), var(--deep-red));
    border-right: 4px solid #d9d9d9;
  }
  .tab--right { top: 28px; right: 0; border-right: none; border-left: 4px solid #d9d9d9; }
  .tab--left { top: 148px; left: 0; }
  .brand {
    position: absolute;
    inset: 0;
    display: flex;
    flex-direction: column;
    align-items: center;
    padding-top: 82px;
  }
  .brand__name {
    display: flex;
    align-items: center;
    gap: 10px;
    color: var(--brand-red);
    font-size: 30px;
    font-weight: 700;
    letter-spacing: 0.5px;
    margin-bottom: 44px;
  }
  .brand__mark {
    width: 18px;
    height: 18px;
    background: var(--brand-red);
  }
  .brand__tagline {
    width: 380px;
    text-align: center;
    font-size: 14.5px;
    font-weight: 600;
    line-height: 1.45;
    color: var(--text-white);
  }
</style>
</head>
<body>
  <main class="canvas">
    <section class="card card--contact" aria-label="Business card, contact side">
      <div class="band band--top"></div>
      <div class="contact">
        <p class="contact__name">Dean Halloway</p>
        <p class="contact__abn"><span class="contact__abn-label">ABN</span> 58 214 937 062</p>
        <p class="contact__line">0417 286 531</p>
        <p class="contact__line">summitgutters@mailbrook.com</p>
        <p class="contact__line">www.summitgutters.com.au</p>
      </div>
      <div class="band band--bottom"></div>
    </section>

    <section class="card card--brand" aria-label="Business card, brand side">
      <div class="tab tab--right"></div>
      <div class="tab tab--left"></div>
      <div class="brand">
        <p class="brand__name"><span class="brand__mark"></span>Summit Gutters Pty Ltd</p>
        <p class="brand__tagline">For all of your metal roof plumbing requirements contact Summit Gutters for an obligation free quote - no job too big or to small!</p>
      </div>
    </section>
  </main>
</body>
</html>
```